Velunor Jobs portal

Velunor Jobs is a job portal connecting job seekers and companies offering part time jobs in the Mena region, starting in the UAE. We would like to see designs that use the color blue. We have attached images to give an idea what the website should look like. When a company posts a job the job seekers are not allowed to see which company has posted a job. There should also be a quintrex gateway. On the landing page we want a catching picture that we will send.

Target Market(s)

Students and promotional workers

Logo Text

Velunor Jobs

Coding

Coded - Design and coding required

Number of Pages Required

4 page

Font styles to use
Sans Serif

Colors
33a6d7
0692cd
85cae6

```html
<!DOCTYPE html>
<html lang="en">
<head>
<meta charset="utf-8">
<title>Velunor Jobs — Job Listings</title>
<link rel="stylesheet" href="https://fonts.googleapis.com/css2?family=Open+Sans:wght@400;600&family=Roboto:wght@400;500&display=swap">
<style>
:root{
  --page-bg:#ecebec;
  --white:#ffffff;
  --text:#4a4a4a;
  --text-dark:#333333;
  --brand:#33a6d7;
  --category-blue:#3565b0;
  --apply-blue:#2f62c0;
  --apply-shadow:#1f4590;
  --accent-purple:#8a44a8;
  --accent-purple-dark:#6b2f86;
  --logout-pink:#e8347a;
  --logout-shadow:#c21f60;
  --line:#e4e4e4;
  --row-alt:#f5f5f5;
  --footer-bg:#2f2f2f;
  --star:#f2a51a;
}
*{box-sizing:border-box;margin:0;padding:0}
html,body{width:1200px;height:1103px;overflow:hidden}
body{background:var(--page-bg);font-family:"Open Sans",sans-serif;color:var(--text);position:relative}

.site-header{position:absolute;left:0;top:0;width:1200px;height:120px;background:linear-gradient(#ffffff,#f3f3f3);border-bottom:1px solid #dcdcdc}
.brand-name{position:absolute;left:97px;top:40px;font-family:"Roboto",sans-serif;font-weight:400;font-size:36px;color:var(--brand);letter-spacing:.5px}
.main-nav{position:absolute;left:348px;top:49px;display:flex;font-family:"Roboto",sans-serif;font-size:15px;color:var(--text)}
.main-nav a{color:inherit;text-decoration:none;padding:0 16px 0 0}
.main-nav a+a{padding-left:18px;border-left:1px solid #e2e2e2}
.header-tools{position:absolute;left:860px;top:38px;width:240px;height:44px}
.icon-search{position:absolute;left:0;top:10px}
.icon-bell{position:absolute;left:46px;top:8px}
.badge{position:absolute;left:58px;top:5px;width:18px;height:18px;border-radius:50%;background:#f0484b;color:#fff;font-size:9px;line-height:18px;text-align:center;font-family:"Roboto",sans-serif}
.avatar{position:absolute;left:90px;top:2px;width:40px;height:40px;border-radius:50%;background:radial-gradient(circle at 50% 40%,#b9b9b9,#7e7e7e);border:2px solid #e6e6e6}
.btn-logout{position:absolute;left:144px;top:6px;width:96px;height:38px;background:var(--logout-pink);border-bottom:3px solid var(--logout-shadow);border-radius:2px;color:#fff;font-family:"Roboto",sans-serif;font-size:15px;text-align:center;line-height:36px}

.category-panel{position:absolute;left:96px;top:163px;width:265px;height:469px;background:var(--white);box-shadow:0 1px 3px rgba(0,0,0,.15)}
.category-panel h2{height:55px;background:var(--category-blue);color:#fff;font-family:"Roboto",sans-serif;font-weight:400;font-size:18px;line-height:55px;padding-left:21px}
.category-list{list-style:none;padding:12px 0 0 20px}
.category-list li{height:31px;font-size:14.5px;color:var(--text-dark);display:flex;align-items:center}
.category-list li::before{content:"";width:7px;height:7px;border:1.5px solid #333;border-radius:50%;margin-right:20px}

.filter-panel{position:absolute;left:396px;top:161px;width:705px;height:100px;background:var(--white);box-shadow:0 1px 3px rgba(0,0,0,.15)}
.field{position:absolute;top:32px;width:257px;height:40px;border:1px solid #cfcfcf;border-radius:2px;font-size:13px;line-height:38px;padding-left:15px}
.field-keyword{left:23px;color:var(--text-dark)}
.field-district{left:297px;color:var(--accent-purple)}
.field-district::after{content:"";position:absolute;right:14px;top:17px;border:5px solid transparent;border-top:6px solid #222}
.btn-filter{position:absolute;left:576px;top:32px;width:106px;height:43px;background:var(--accent-purple);border-bottom:3px solid var(--accent-purple-dark);border-radius:2px;color:#fff;font-family:"Roboto",sans-serif;font-size:15px;text-align:center;line-height:40px}

.job-table{position:absolute;left:396px;top:271px;width:705px;border-collapse:collapse;background:var(--white);box-shadow:0 1px 3px rgba(0,0,0,.15)}
.job-table th{height:64px;background:#f4f4f4;color:var(--accent-purple);font-family:"Roboto",sans-serif;font-weight:400;font-size:15.5px;text-align:left;padding-left:23px;border-bottom:1px solid var(--line);border-right:1px solid var(--line)}
.job-table td{font-size:12.5px;color:var(--text-dark);padding-left:23px;border-right:1px solid #eeeeee}
.job-table th:nth-child(3),.job-table td:nth-child(3){padding-left:40px}
.job-table th:last-child,.job-table td:last-child{border-right:none}
.job-table td.job-title{font-size:15px;color:var(--text)}
.job-table tr:nth-child(even) td{background:var(--row-alt)}
.btn-apply{display:inline-block;margin-left:13px;width:96px;height:39px;background:var(--apply-blue);border-bottom:3px solid var(--apply-shadow);border-radius:3px;color:#fff;font-family:"Open Sans",sans-serif;font-weight:600;font-size:13.5px;text-align:center;line-height:36px}

.mascot{position:absolute;left:94px;top:677px;width:223px;height:287px;border-radius:45% 45% 30% 30%;background:radial-gradient(ellipse at 50% 40%,#dedddf,#ecebec 70%)}

.featured{position:absolute;left:398px;top:690px;width:705px}
.featured h2{font-family:"Roboto",sans-serif;font-weight:400;font-size:26px;color:var(--accent-purple)}
.carousel-arrows{position:absolute;right:2px;top:6px}
.provider-cards{position:absolute;left:1px;top:60px;display:flex;gap:15px}
.provider-card{width:165px}
.provider-photo{height:127px;box-shadow:0 1px 3px rgba(0,0,0,.25)}
.photo-1{background:linear-gradient(135deg,#a79b88,#5b6f8a)}
.photo-2{background:linear-gradient(135deg,#9ec6de,#e3e8ee)}
.photo-3{background:linear-gradient(135deg,#1c4f78,#3ab0d8)}
.photo-4{background:linear-gradient(135deg,#c5d3dc,#3a4250)}
.provider-card p{margin-top:14px;font-size:14.5px;color:var(--text)}
.stars{margin-top:4px;display:flex;gap:1px}

.site-footer{position:absolute;left:0;top:978px;width:1200px;height:125px;background:var(--footer-bg);color:#fff}
.footer-links{position:absolute;left:99px;top:40px;font-family:"Roboto",sans-serif;font-size:13.5px}
.footer-links span{margin:0 5px}
.copyright{position:absolute;left:99px;top:67px;font-family:"Roboto",sans-serif;font-size:15px}
.social{position:absolute;left:937px;top:46px;display:flex;gap:8px}
.social span{width:34px;height:34px;border-radius:2px}
.social .s1{background:#2aa3e0}
.social .s2{background:#d8302b}
.social .s3{background:#3b5b9a}
.social .s4{background:#1b7cc0}
</style>
</head>
<body>
<header class="site-header">
  <div class="brand-name">Velunor Jobs</div>
  <nav class="main-nav"><a href="#">About Us</a><a href="#">Contact Us</a></nav>
  <div class="header-tools">
    <svg class="icon-search" width="26" height="26" viewBox="0 0 26 26"><circle cx="10" cy="10" r="8" fill="none" stroke="#333" stroke-width="2.6"/><line x1="16" y1="16" x2="23" y2="23" stroke="#333" stroke-width="2.8" stroke-linecap="round"/></svg>
    <svg class="icon-bell" width="26" height="28" viewBox="0 0 26 28"><path d="M5 20V12a8 8 0 0 1 16 0v8l2 2H3z" fill="none" stroke="#333" stroke-width="1.8" stroke-linejoin="round"/><path d="M10 24a3 3 0 0 0 6 0" fill="none" stroke="#333" stroke-width="1.8"/></svg>
    <div class="badge">10</div>
    <div class="avatar" role="img" aria-label="User profile photo"></div>
    <div class="btn-logout">LOG OUT</div>
  </div>
</header>

<aside class="category-panel">
  <h2>CATEGORY</h2>
  <ul class="category-list">
    <li>Category 1 (33)</li><li>Category 2 (33)</li><li>Category 4 (303)</li><li>Category 5 (150)</li>
    <li>Category 6 (31)</li><li>Category 7 (201)</li><li>Category 1 (33)</li><li>Category 2 (33)</li>
    <li>Category 4 (303)</li><li>Category 5 (150)</li><li>Category 6 (31)</li><li>Category 7 (201)</li>
  </ul>
</aside>

<section class="filter-panel">
  <div class="field field-keyword">Keyword</div>
  <div class="field field-district">District 1</div>
  <div class="btn-filter">FILTER JOB</div>
</section>

<table class="job-table">
  <colgroup><col style="width:224px"><col style="width:137px"><col style="width:163px"><col></colgroup>
  <tr><th>Job Title</th><th>Due Date</th><th>Provider Name</th><th></th></tr>
  <tr style="height:82px"><td class="job-title">Front-end Developer</td><td>23-05-15</td><td>Provider 1</td><td><span class="btn-apply">Apply Now</span></td></tr>
  <tr style="height:74px"><td class="job-title">Front-end Developer</td><td>23-05-15</td><td>Provider 1</td><td><span class="btn-apply">Apply Now</span></td></tr>
  <tr style="height:74px"><td class="job-title">Front-end Developer</td><td>23-05-15</td><td>Provider 1</td><td><span class="btn-apply">Apply Now</span></td></tr>
  <tr style="height:73px"><td class="job-title">Front-end Developer</td><td>23-05-15</td><td>Provider 1</td><td><span class="btn-apply">Apply Now</span></td></tr>
</table>

<div class="mascot" role="img" aria-label="Faint mascot illustration of a flying caped character"></div>

<section class="featured">
  <h2>Featured Job Providers</h2>
  <svg class="carousel-arrows" width="46" height="26" viewBox="0 0 46 26"><polyline points="13,2 3,13 13,24" fill="none" stroke="#555" stroke-width="2"/><polyline points="33,2 43,13 33,24" fill="none" stroke="#555" stroke-width="2"/></svg>
  <div class="provider-cards">
    <div class="provider-card"><div class="provider-photo photo-1" role="img" aria-label="Photo of a woman using a tablet"></div><p>Duis aute irure dolor in</p><svg class="stars" width="60" height="10" viewBox="0 0 60 10"><g fill="#f2a51a"><polygon points="5,0 6.5,3.5 10,3.8 7.3,6 8.1,9.5 5,7.6 1.9,9.5 2.7,6 0,3.8 3.5,3.5"/><polygon transform="translate(12 0)" points="5,0 6.5,3.5 10,3.8 7.3,6 8.1,9.5 5,7.6 1.9,9.5 2.7,6 0,3.8 3.5,3.5"/><polygon transform="translate(24 0)" points="5,0 6.5,3.5 10,3.8 7.3,6 8.1,9.5 5,7.6 1.9,9.5 2.7,6 0,3.8 3.5,3.5"/></g><g fill="none" stroke="#bbb" stroke-width=".8"><polygon transform="translate(36 0)" points="5,0 6.5,3.5 10,3.8 7.3,6 8.1,9.5 5,7.6 1.9,9.5 2.7,6 0,3.8 3.5,3.5"/><polygon transform="translate(48 0)" points="5,0 6.5,3.5 10,3.8 7.3,6 8.1,9.5 5,7.6 1.9,9.5 2.7,6 0,3.8 3.5,3.5"/></g></svg></div>
    <div class="provider-card"><div class="provider-photo photo-2" role="img" aria-label="Photo of a hand touching a tablet with flying pages"></div><p>Duis aute irure dolor in</p><svg class="stars" width="60" height="10" viewBox="0 0 60 10"><g fill="#f2a51a"><polygon points="5,0 6.5,3.5 10,3.8 7.3,6 8.1,9.5 5,7.6 1.9,9.5 2.7,6 0,3.8 3.5,3.5"/><polygon transform="translate(12 0)" points="5,0 6.5,3.5 10,3.8 7.3,6 8.1,9.5 5,7.6 1.9,9.5 2.7,6 0,3.8 3.5,3.5"/><polygon transform="translate(24 0)" points="5,0 6.5,3.5 10,3.8 7.3,6 8.1,9.5 5,7.6 1.9,9.5 2.7,6 0,3.8 3.5,3.5"/></g><g fill="none" stroke="#bbb" stroke-width=".8"><polygon transform="translate(36 0)" points="5,0 6.5,3.5 10,3.8 7.3,6 8.1,9.5 5,7.6 1.9,9.5 2.7,6 0,3.8 3.5,3.5"/><polygon transform="translate(48 0)" points="5,0 6.5,3.5 10,3.8 7.3,6 8.1,9.5 5,7.6 1.9,9.5 2.7,6 0,3.8 3.5,3.5"/></g></svg></div>
    <div class="provider-card"><div class="provider-photo photo-3" role="img" aria-label="Photo of a businessman holding a glowing globe above a tablet"></div><p>Duis aute irure dolor in</p><svg class="stars" width="60" height="10" viewBox="0 0 60 10"><g fill="#f2a51a"><polygon points="5,0 6.5,3.5 10,3.8 7.3,6 8.1,9.5 5,7.6 1.9,9.5 2.7,6 0,3.8 3.5,3.5"/><polygon transform="translate(12 0)" points="5,0 6.5,3.5 10,3.8 7.3,6 8.1,9.5 5,7.6 1.9,9.5 2.7,6 0,3.8 3.5,3.5"/><polygon transform="translate(24 0)" points="5,0 6.5,3.5 10,3.8 7.3,6 8.1,9.5 5,7.6 1.9,9.5 2.7,6 0,3.8 3.5,3.5"/></g><g fill="none" stroke="#bbb" stroke-width=".8"><polygon transform="translate(36 0)" points="5,0 6.5,3.5 10,3.8 7.3,6 8.1,9.5 5,7.6 1.9,9.5 2.7,6 0,3.8 3.5,3.5"/><polygon transform="translate(48 0)" points="5,0 6.5,3.5 10,3.8 7.3,6 8.1,9.5 5,7.6 1.9,9.5 2.7,6 0,3.8 3.5,3.5"/></g></svg></div>
    <div class="provider-card"><div class="provider-photo photo-4" role="img" aria-label="Photo of three business people reviewing a folder"></div><p>Duis aute irure dolor in</p><svg class="stars" width="60" height="10" viewBox="0 0 60 10"><g fill="#f2a51a"><polygon points="5,0 6.5,3.5 10,3.8 7.3,6 8.1,9.5 5,7.6 1.9,9.5 2.7,6 0,3.8 3.5,3.5"/><polygon transform="translate(12 0)" points="5,0 6.5,3.5 10,3.8 7.3,6 8.1,9.5 5,7.6 1.9,9.5 2.7,6 0,3.8 3.5,3.5"/><polygon transform="translate(24 0)" points="5,0 6.5,3.5 10,3.8 7.3,6 8.1,9.5 5,7.6 1.9,9.5 2.7,6 0,3.8 3.5,3.5"/></g><g fill="none" stroke="#bbb" stroke-width=".8"><polygon transform="translate(36 0)" points="5,0 6.5,3.5 10,3.8 7.3,6 8.1,9.5 5,7.6 1.9,9.5 2.7,6 0,3.8 3.5,3.5"/><polygon transform="translate(48 0)" points="5,0 6.5,3.5 10,3.8 7.3,6 8.1,9.5 5,7.6 1.9,9.5 2.7,6 0,3.8 3.5,3.5"/></g></svg></div>
  </div>
</section>

<footer class="site-footer">
  <div class="footer-links">About<span>|</span>Disclaimer<span>|</span>Contact<span>|</span>Sitemap</div>
  <div class="copyright">Copyright © 2015&nbsp; All Rights</div>
  <div class="social"><span class="s1"></span><span class="s2"></span><span class="s3"></span><span class="s4"></span></div>
</footer>
</body>
</html>
```